Vornel Technologies business card design

We need a business card designed with our new logo. it would be great if the card could communicate it is a technology based company.

Target Market(s)

system integrators

Industry/Entity Type

technology, IOT

Contact Information for Business Card

Name, designation, Address, telephone number, email address

Requirements
Must have
• logo and company name
Nice to have
• something to do with technology

```html
<!DOCTYPE html>
<html lang="en">
<head>
<meta charset="utf-8">
<title>Vornel Technologies – Business Card</title>
<link href="https://fonts.googleapis.com/css2?family=Ubuntu:wght@400;500;700&display=swap" rel="stylesheet">
<style>
  :root {
    --orange: #f7941d;
    --charcoal: #39393b;
    --white: #ffffff;
    --backdrop: #d9d9d9;
    --text-dark: #3b3b3d;
  }
  * { margin: 0; padding: 0; box-sizing: border-box; }
  html, body {
    width: 1055px; height: 1200px; overflow: hidden;
    background: var(--backdrop);
    font-family: "Ubuntu", sans-serif;
  }
  .canvas { position: relative; width: 1055px; height: 1200px; }
  .card {
    position: absolute; left: 77px; width: 900px; height: 515px;
    overflow: hidden;
    box-shadow: 0 6px 18px rgba(0,0,0,0.18);
  }
  .card--front { top: 55px; background: var(--white); }
  .card--back { top: 630px; background: var(--charcoal); }
  .card__band { position: absolute; inset: 0; width: 100%; height: 100%; }

  .brand { position: absolute; display: flex; align-items: center; gap: 14px; }
  .brand__square { width: 22px; height: 22px; background: var(--orange); flex: none; }
  .brand__name {
    font-weight: 700; font-size: 42px; line-height: 1;
    letter-spacing: 0.5px; white-space: nowrap;
  }
  .card--front .brand { left: 55px; top: 70px; }
  .card--front .brand__name { color: var(--text-dark); }
  .card--back .brand { right: 52px; top: 110px; }
  .card--back .brand__name { color: var(--white); }

  .person { position: absolute; left: 58px; top: 218px; }
  .person__name {
    color: var(--orange); font-weight: 700; font-size: 51px; line-height: 1;
    white-space: nowrap;
  }
  .person__role {
    color: var(--text-dark); font-size: 27px; line-height: 1; margin-top: 14px;
  }
  .contact { position: absolute; left: 58px; top: 342px; list-style: none; }
  .contact__item {
    display: flex; align-items: center; gap: 14px;
    color: var(--text-dark); font-size: 27px; line-height: 37px;
    white-space: nowrap;
  }
  .contact__icon { width: 18px; height: 18px; flex: none; fill: var(--orange); }

  .web {
    position: absolute; right: 52px; bottom: 84px;
    color: var(--white); font-size: 27px; letter-spacing: 0.5px;
  }
</style>
</head>
<body>
<main class="canvas">

  <section class="card card--front" aria-label="Business card front">
    <svg class="card__band" viewBox="0 0 900 515" aria-hidden="true">
      <polygon points="700,515 840,0 900,0 900,515" fill="var(--charcoal)"/>
      <polygon points="640,515 780,0 820,0 680,515" fill="var(--orange)"/>
    </svg>

    <div class="brand">
      <span class="brand__square"></span>
      <span class="brand__name">Vornel Technologies</span>
    </div>

    <div class="person">
      <p class="person__name">PLACE NAME HERE</p>
      <p class="person__role">Position Here</p>
    </div>

    <ul class="contact">
      <li class="contact__item">
        <svg class="contact__icon" viewBox="0 0 24 24"><path d="M12 1a8 8 0 0 0-8 8c0 6 8 14 8 14s8-8 8-14a8 8 0 0 0-8-8zm0 11a3 3 0 1 1 0-6 3 3 0 0 1 0 6z"/></svg>
        address
      </li>
      <li class="contact__item">
        <svg class="contact__icon" viewBox="0 0 24 24"><path d="M6.6 2.5l3 .5 1 5-2.3 1.6a12 12 0 0 0 6.1 6.1L16 13.4l5 1 .5 3c0 1.8-1.8 3.6-3.6 3.3C10 19.6 4.4 14 3.3 6.1 3 4.3 4.8 2.5 6.6 2.5z"/></svg>
        telephone number
      </li>
      <li class="contact__item">
        <svg class="contact__icon" viewBox="0 0 24 24"><path d="M2 5h20v14H2z" fill="var(--orange)"/><path d="M2 5l10 8 10-8" fill="none" stroke="var(--white)" stroke-width="2"/></svg>
        email address
      </li>
    </ul>
  </section>

  <section class="card card--back" aria-label="Business card back">
    <svg class="card__band" viewBox="0 0 900 515" aria-hidden="true">
      <polygon points="0,0 200,0 60,515 0,515" fill="var(--orange)"/>
      <polygon points="240,0 280,0 140,515 100,515" fill="var(--white)"/>
    </svg>

    <div class="brand">
      <span class="brand__square"></span>
      <span class="brand__name">Vornel Technologies</span>
    </div>

    <p class="web">webaddress.com</p>
  </section>

</main>
</body>
</html>
```